Water Filtration Company needs a business card design using our existing logo/colours!

We design and manufacture and export specialised water filtration equipment. Our equipment will take unclean dirty water and filters to safe clean drinkable water.
We would like to see designs using our existing logo and colours (see attached "Palette") that represents clean safe drinking water (fresh, clean designs but still professional and modern). Our customers are other businesses who supply water filtration equipment, governments, and private individuals.
BUSINESS CARD DETAILS (Common details):
Tel: + 61 7 55 419 276
www: brindlepeak.com.au
Address: 3/47 Cordwell Parade
Marlow Flats NSW 2593 Australia
(please include the word Australia as we are an international company)
Must include: COMMERCIAL WATER FILTRATION EQUIPMENT
NAME NO 1:
Owen Pritch
General Manager
Mobile: +61 427 38 91 04
Email: owen@brindlepeak.com.au
NAME NO. 2:
Gina Rosk
Business Manager
Mobile: +61 409 572 148
Email: gina@brindlepeak.com.au
Must Have:
1) PRINT READY IN .AI & .PDF FORMATS
2) Also saved in file format .ai (Adobe Illustrator - compatible with CS4)
3) Use existing LOGO & COLOURS: Please use our logo (see attached file)
4) FONTS: we have used Avenir & Helvetica in the past but are open to other font types for the address etc.
Thank you!

```html
<!DOCTYPE html>
<html lang="en">
<head>
<meta charset="utf-8">
<title>Brindle Peak – Business Cards</title>
<link rel="stylesheet" href="https://fonts.googleapis.com/css2?family=Montserrat:ital,wght@0,400;0,500;0,600;1,400&display=swap">
<style>
  :root {
    --bg: #e6e8ea;
    --card: #ffffff;
    --teal-light: #1f9dbd;
    --teal-dark: #0d6487;
    --brand: #137fa4;
    --stripe: #9b9fa3;
    --ink: #3c4246;
    --ink-soft: #6a7074;
    --on-teal: #ffffff;
  }
  * { box-sizing: border-box; margin: 0; padding: 0; }
  html, body {
    width: 1200px; height: 901px; overflow: hidden;
    background: var(--bg);
    font-family: "Montserrat", Arial, sans-serif;
  }
  .stage { position: relative; width: 1200px; height: 901px; }
  .card {
    position: absolute; width: 520px; height: 300px;
    background: var(--card); border-radius: 24px; overflow: hidden;
    box-shadow: 0 6px 18px rgba(0,0,0,.14);
  }
  .card--owen { left: 60px; top: 120px; }
  .card--gina { left: 60px; top: 480px; }
  .card--back { left: 620px; top: 300px; }
  .card__wave { position: absolute; inset: 0; width: 100%; height: 100%; }
  .person { position: absolute; left: 36px; top: 42px; }
  .person__name {
    font-size: 17px; font-weight: 500; letter-spacing: .12em;
    color: var(--ink); text-transform: uppercase;
  }
  .person__role { margin-top: 6px; font-size: 11px; font-style: italic; color: var(--ink-soft); }
  .brand-block { display: flex; flex-direction: column; align-items: flex-end; }
  .brand {
    display: flex; align-items: center; gap: 10px;
    color: var(--brand); font-weight: 500; white-space: nowrap;
  }
  .brand__dot { border-radius: 50%; background: var(--brand); flex: none; }
  .tagline {
    color: var(--brand); font-weight: 600; text-transform: uppercase;
    letter-spacing: .12em; white-space: nowrap;
  }
  .card--front .brand-block { position: absolute; right: 34px; top: 34px; }
  .card--front .brand { font-size: 30px; }
  .card--front .brand__dot { width: 12px; height: 12px; }
  .card--front .tagline { margin-top: 4px; font-size: 7.5px; }
  .card--back .brand-block {
    position: absolute; left: 50%; top: 50%; transform: translate(-50%, -50%);
    align-items: center;
  }
  .card--back .brand { font-size: 44px; }
  .card--back .brand__dot { width: 16px; height: 16px; }
  .card--back .tagline { margin-top: 8px; font-size: 11px; }
  .contact {
    position: absolute; right: 30px; bottom: 20px;
    list-style: none; text-align: right;
    color: var(--on-teal); font-size: 10.5px; line-height: 15px; letter-spacing: .02em;
  }
  .contact li { display: flex; justify-content: flex-end; align-items: center; gap: 8px; }
  .contact__icon { width: 10px; height: 10px; flex: none; }
  .contact__spacer { width: 10px; flex: none; }
</style>
</head>
<body>
<main class="stage">
  <svg width="0" height="0" style="position:absolute" aria-hidden="true">
    <defs>
      <linearGradient id="tealFill" x1="0" y1="0" x2="1" y2="1">
        <stop offset="0" stop-color="#0d6487"/>
        <stop offset="1" stop-color="#1f9dbd"/>
      </linearGradient>
      <symbol id="wave" viewBox="0 0 520 300" preserveAspectRatio="none">
        <path d="M0 112 C150 126 330 150 520 160 L520 176 C330 162 150 136 0 124 Z" fill="#9b9fa3"/>
        <path d="M0 126 C150 138 330 164 520 180 L520 300 L0 300 Z" fill="url(#tealFill)"/>
      </symbol>
      <symbol id="icon-pin" viewBox="0 0 10 10"><path d="M5 0.5a3.2 3.2 0 0 0-3.2 3.2C1.8 6 5 9.5 5 9.5S8.2 6 8.2 3.7A3.2 3.2 0 0 0 5 .5Zm0 4.4a1.2 1.2 0 1 1 0-2.4 1.2 1.2 0 0 1 0 2.4Z" fill="currentColor"/></symbol>
      <symbol id="icon-phone" viewBox="0 0 10 10"><path d="M2.2 .8 3.6 2.6 2.8 3.6C3.4 4.9 5 6.5 6.4 7.2l1-.8 1.8 1.4-.9 1.4C4.6 9 1 5.4.8 1.7Z" fill="currentColor"/></symbol>
      <symbol id="icon-mobile" viewBox="0 0 10 10"><rect x="2.5" y=".5" width="5" height="9" rx="1" fill="none" stroke="currentColor"/><circle cx="5" cy="7.8" r=".6" fill="currentColor"/></symbol>
      <symbol id="icon-mail" viewBox="0 0 10 10"><rect x=".5" y="2" width="9" height="6" fill="none" stroke="currentColor"/><path d="M.5 2 5 5.5 9.5 2" fill="none" stroke="currentColor"/></symbol>
      <symbol id="icon-web" viewBox="0 0 10 10"><circle cx="5" cy="5" r="4.4" fill="none" stroke="currentColor"/><path d="M.6 5h8.8M5 .6c-2.4 2.6-2.4 6.2 0 8.8M5 .6c2.4 2.6 2.4 6.2 0 8.8" fill="none" stroke="currentColor" stroke-width=".7"/></symbol>
    </defs>
  </svg>

  <section class="card card--front card--owen" aria-label="Business card front, Owen Pritch">
    <svg class="card__wave" aria-hidden="true"><use href="#wave"/></svg>
    <div class="person">
      <p class="person__name">Owen Pritch</p>
      <p class="person__role">General Manager</p>
    </div>
    <div class="brand-block">
      <div class="brand"><span class="brand__dot"></span><span class="brand__name">Brindle Peak</span></div>
      <p class="tagline">Commercial Water Filtration Equipment</p>
    </div>
    <ul class="contact">
      <li><span>3/47 Cordwell Parade</span><span class="contact__spacer"></span></li>
      <li><span>Marlow Flats NSW 2593 Australia</span><svg class="contact__icon" aria-hidden="true"><use href="#icon-pin"/></svg></li>
      <li><span>+ 61 7 55 419 276</span><svg class="contact__icon" aria-hidden="true"><use href="#icon-phone"/></svg></li>
      <li><span>+61 427 38 91 04</span><svg class="contact__icon" aria-hidden="true"><use href="#icon-mobile"/></svg></li>
      <li><span>owen@brindlepeak.com.au</span><svg class="contact__icon" aria-hidden="true"><use href="#icon-mail"/></svg></li>
      <li><span>brindlepeak.com.au</span><svg class="contact__icon" aria-hidden="true"><use href="#icon-web"/></svg></li>
    </ul>
  </section>

  <section class="card card--front card--gina" aria-label="Business card front, Gina Rosk">
    <svg class="card__wave" aria-hidden="true"><use href="#wave"/></svg>
    <div class="person">
      <p class="person__name">Gina Rosk</p>
      <p class="person__role">Business Manager</p>
    </div>
    <div class="brand-block">
      <div class="brand"><span class="brand__dot"></span><span class="brand__name">Brindle Peak</span></div>
      <p class="tagline">Commercial Water Filtration Equipment</p>
    </div>
    <ul class="contact">
      <li><span>3/47 Cordwell Parade</span><span class="contact__spacer"></span></li>
      <li><span>Marlow Flats NSW 2593 Australia</span><svg class="contact__icon" aria-hidden="true"><use href="#icon-pin"/></svg></li>
      <li><span>+ 61 7 55 419 276</span><svg class="contact__icon" aria-hidden="true"><use href="#icon-phone"/></svg></li>
      <li><span>+61 409 572 148</span><svg class="contact__icon" aria-hidden="true"><use href="#icon-mobile"/></svg></li>
      <li><span>gina@brindlepeak.com.au</span><svg class="contact__icon" aria-hidden="true"><use href="#icon-mail"/></svg></li>
      <li><span>brindlepeak.com.au</span><svg class="contact__icon" aria-hidden="true"><use href="#icon-web"/></svg></li>
    </ul>
  </section>

  <section class="card card--back" aria-label="Business card back">
    <div class="brand-block">
      <div class="brand"><span class="brand__dot"></span><span class="brand__name">Brindle Peak</span></div>
      <p class="tagline">Commercial Water Filtration Equipment</p>
    </div>
  </section>
</main>
</body>
</html>
```